General Contractor Website Design

We are working with a General Contractor in California that specializes in building custom kitchens, baths, and homes for high-end clients.

Here are some websites for inspiration:
https://mervalstudio.com/
https://ridgelorebuilders.com
https://www.framplank.com
https://www.quellnest.com
https://www.zelhaus.com
https://plyestates.com

Thank you for taking the time to consider designing a website for us. We are web developers based in Stockton, CA, USA. Most of our projects go through the same process. Understanding this process may help you win a project with us. We custom-code all of our websites in-house. We don’t have any requirements as to what tools you use for your design, but we ask that you follow these guidelines.

IMAGES:
If you use any images or icons in the design, we ask that you have a link to the asset so we can purchase the image/icon. Most of the designs we submit do not have the customer’s images on them unless they have some great images. Be creative; show us the feeling you are trying to portray with your image choices. Use any royalty-free site you choose. We subscribe to Vantrix and mainly use their images, but we can purchase images outside of Vantrix. PLEASE NOTE: we will not submit designs to clients with watermarks on the images.

FONTS:
We ask that you identify the fonts you’re using in the design. This can be done in a message if you want. We typically use Orlimo Fonts and Vantrix Fonts.

CONTENT:
We're always open to different content and ideas. We often submit designs with stock images so the client can see our vision. We typically take pictures after the website launch to use their images with our vision. Lorem Ipsum is fine for paragraphs, but we ask that you make the Headers with correct English. We want to be able to show the vision and identify the sections of the website.

INSPIRATION:
We typically add a couple of links in the brief of websites we like to help you get started in your design.

REVISIONS:
We do not often ask for revisions of the designs unless we see something in the design that may not appeal to the client. If there are slight changes that we want to make, we do that in the development process.

FEEDBACK:
We rarely give feedback on designs during the design process. We are working on many website projects and do not have the time to provide feedback. We usually respond if your request is well thought out and asks specific questions, but a note asking “feedback, please” usually goes unanswered.

```html
<!DOCTYPE html>
<html lang="en">
<head>
<meta charset="utf-8">
<title>Oakline Builders</title>
<link rel="stylesheet" href="https://fonts.googleapis.com/css2?family=Poppins:wght@400;500;600;700;800&display=swap">
<style>
:root{
  --red:#b81c2e;
  --ink:#111111;
  --text:#222222;
  --muted:#777777;
  --field:#e6e6e6;
  --field-line:#c9c9c9;
  --about-bg:#c9bfc2;
  --project-bg:#f7e6e8;
  --white:#ffffff;
}
*{box-sizing:border-box;margin:0;padding:0}
html,body{width:1200px;height:3345px;overflow:hidden;background:var(--white);font-family:'Poppins',sans-serif;color:var(--text)}
.page{position:relative;width:1200px;height:3345px}
.brand{display:flex;align-items:center;gap:12px}
.brand-mark{width:30px;height:30px;background:var(--red)}
.brand-name{font-weight:700;color:var(--red);letter-spacing:3px;text-transform:uppercase}
/* header + hero */
.hero{position:absolute;left:0;top:0;width:1200px;height:684px;background:var(--red)}
.hero-photo{position:absolute;left:0;top:0;width:1200px;height:684px;clip-path:polygon(3px 0,1196px 0,1185px 665px,25px 665px);
  background:
    radial-gradient(ellipse 190px 150px at 560px 420px,rgba(255,196,120,.55),rgba(255,196,120,0) 70%),
    radial-gradient(ellipse 120px 90px at 360px 430px,rgba(255,210,140,.35),rgba(255,210,140,0) 70%),
    radial-gradient(ellipse 120px 90px at 790px 420px,rgba(255,210,140,.35),rgba(255,210,140,0) 70%),
    radial-gradient(ellipse 260px 380px at 60px 300px,rgba(24,34,26,.9),rgba(24,34,26,0) 75%),
    radial-gradient(ellipse 260px 380px at 1150px 300px,rgba(30,40,32,.85),rgba(30,40,32,0) 75%),
    radial-gradient(ellipse 420px 220px at 600px 260px,rgba(70,80,110,.8),rgba(70,80,110,0) 75%),
    linear-gradient(180deg,#2c3038 0%,#3c4356 30%,#4a4f5c 52%,#5d5a52 68%,#465a33 82%,#3a4a2a 100%)}
.hero-shade{position:absolute;left:0;top:0;width:1200px;height:684px;background:linear-gradient(180deg,rgba(0,0,0,.15),rgba(0,0,0,0) 60%);clip-path:polygon(3px 0,1196px 0,1185px 665px,25px 665px)}
.topbar{position:absolute;left:0;top:0;width:1200px;height:92px;background:rgba(235,235,240,.9)}
.topbar .brand{position:absolute;left:114px;top:28px}
.topbar .brand-name{font-size:26px}
.nav{position:absolute;left:604px;top:33px;display:flex;gap:29px;font-size:15px;letter-spacing:.5px}
.nav a{color:var(--ink);text-decoration:none}
.nav a.active{color:var(--red);font-weight:600;border-bottom:2px solid var(--red);padding-bottom:3px}
.hero-title{position:absolute;left:0;top:193px;width:1200px;text-align:center;color:var(--white);font-weight:800;font-size:70px;line-height:94px;letter-spacing:1px;text-shadow:0 2px 8px rgba(0,0,0,.35)}
/* about */
.about{position:absolute;left:0;top:684px;width:1200px;height:685px;background:linear-gradient(180deg,#c4babd 0%,#cbc1c4 45%,#d6cfd0 100%)}
.rule-title{display:flex;align-items:center;justify-content:center;gap:6px;color:var(--red);font-weight:800;font-size:43px}
.rule-title::before,.rule-title::after{content:"";width:60px;height:2px;background:#555}
.about .rule-title{position:absolute;top:50px;left:0;width:1200px}
.about p{position:absolute;left:130px;top:108px;width:940px;text-align:center;font-size:22px;line-height:34px;color:var(--ink)}
.btn{display:flex;align-items:center;justify-content:center;background:var(--ink);color:var(--white);font-size:17px;font-weight:500;border-bottom:4px solid var(--red);border-right:3px solid var(--red)}
.about .btn{position:absolute;left:514px;top:240px;width:172px;height:50px}
.about-photo{position:absolute;left:0;top:296px;width:1200px;height:389px;
  background:
    radial-gradient(ellipse 80px 240px at 210px 260px,rgba(150,150,150,.6),rgba(150,150,150,0) 80%),
    radial-gradient(ellipse 90px 120px at 60px 310px,rgba(70,110,60,.55),rgba(70,110,60,0) 80%),
    radial-gradient(ellipse 70px 120px at 1110px 130px,rgba(110,110,110,.5),rgba(110,110,110,0) 80%),
    radial-gradient(ellipse 260px 70px at 870px 115px,rgba(190,150,115,.75),rgba(190,150,115,0) 80%),
    radial-gradient(ellipse 220px 70px at 430px 115px,rgba(180,130,95,.65),rgba(180,130,95,0) 80%),
    radial-gradient(ellipse 520px 60px at 700px 210px,rgba(238,232,228,.9),rgba(238,232,228,0) 85%),
    linear-gradient(90deg,rgba(176,132,100,.55) 0%,rgba(176,132,100,0) 10%,rgba(176,132,100,0) 90%,rgba(220,215,212,.6) 100%),
    linear-gradient(180deg,#cfc7c7 0%,#e2dbd6 22%,#cfa88a 38%,#e9e4df 58%,#f1eeeb 76%,#d7bfa6 92%,#cbb49b 100%)}
/* services */
.services-title{position:absolute;top:1415px;left:0;width:1200px;text-align:center;color:var(--red);font-weight:800;font-size:43px}
.service{position:absolute;top:1508px;width:260px;text-align:center}
.service .circle{width:231px;height:231px;border-radius:50%;margin:0 auto;box-shadow:0 4px 10px rgba(0,0,0,.18)}
.service h3{margin-top:20px;font-size:18px;line-height:33px;font-weight:700;color:var(--ink)}
.c-bath{background:radial-gradient(circle at 70% 35%,#7a8c6a 0,#7a8c6a 10%,rgba(122,140,106,0) 30%),radial-gradient(ellipse at 35% 78%,#ffffff 0,#f3f1ee 25%,rgba(243,241,238,0) 50%),linear-gradient(140deg,#f2f2f2 0%,#dedbd6 50%,#a9927a 100%)}
.c-kitchen{background:radial-gradient(ellipse at 55% 72%,#3b3733 0,#46413b 28%,rgba(70,65,59,0) 55%),radial-gradient(ellipse at 70% 88%,#c98d55 0,rgba(201,141,85,0) 30%),linear-gradient(170deg,#f2f0ec 0%,#dddad5 45%,#807a72 100%)}
.c-base{background:radial-gradient(ellipse at 40% 60%,#f2f2f0 0,#e2e1de 25%,rgba(226,225,222,0) 50%),radial-gradient(ellipse at 80% 65%,#3d3a38 0,rgba(61,58,56,0) 35%),linear-gradient(170deg,#d8d8d6 0%,#b9b8b5 50%,#6f6d6a 100%)}
.c-bed{background:radial-gradient(ellipse at 60% 72%,#6e4a36 0,#7d5640 20%,rgba(125,86,64,0) 45%),radial-gradient(ellipse at 50% 35%,#f0ebe2 0,rgba(240,235,226,0) 40%),linear-gradient(170deg,#d9cfc2 0%,#b9a38c 55%,#4e3c30 100%)}
/* projects */
.projects{position:absolute;left:0;top:1870px;width:1200px;height:585px;background:var(--project-bg)}
.projects .rule-title{position:absolute;top:44px;left:0;width:1200px}
.projects .rule-title::before,.projects .rule-title::after{width:70px}
.project{position:absolute;top:158px;width:316px;height:306px;display:flex;align-items:flex-end;justify-content:center;padding-bottom:70px;color:var(--white);font-weight:700;font-size:16px;letter-spacing:.5px;text-shadow:0 1px 4px rgba(0,0,0,.4)}
.p-kitchen{background:radial-gradient(ellipse at 50% 82%,#c9a070 0,#b98a58 30%,rgba(185,138,88,0) 60%),radial-gradient(ellipse at 20% 45%,#efe9e1 0,rgba(239,233,225,0) 35%),linear-gradient(170deg,#7a6550 0%,#c09468 45%,#a77c50 100%)}
.p-bath{background:radial-gradient(ellipse at 60% 40%,#8d8b87 0,rgba(141,139,135,0) 40%),radial-gradient(ellipse at 72% 70%,#a67a52 0,rgba(166,122,82,0) 25%),linear-gradient(170deg,#2d2d2d 0%,#4a4844 50%,#7b766f 100%)}
.p-kids{background:radial-gradient(ellipse at 45% 55%,#f2efe9 0,#e2ddd4 25%,rgba(226,221,212,0) 50%),radial-gradient(ellipse at 88% 40%,#b9c0c6 0,rgba(185,192,198,0) 40%),radial-gradient(ellipse at 15% 30%,#8a6446 0,rgba(138,100,70,0) 35%),linear-gradient(170deg,#6d5a48 0%,#a59a8c 55%,#c4bfb6 100%)}
.dots{position:absolute;left:543px;top:494px;width:113px;height:37px;border:1px solid #999;border-radius:8px;background:var(--white);display:flex;align-items:center;justify-content:center;gap:16px}
.dots span{width:10px;height:10px;border-radius:50%;background:var(--ink)}
/* contact */
.contact-title{position:absolute;left:112px;top:2505px;display:flex;align-items:center;gap:6px;color:var(--red);font-weight:800;font-size:43px}
.contact-title::after{content:"";width:75px;height:2px;background:#555}
.contact-text{position:absolute;left:112px;top:2577px;width:460px;font-size:22px;line-height:34px;color:var(--ink)}
.contact-item{position:absolute;left:130px;display:flex;align-items:center;gap:26px;font-size:18px;color:var(--ink)}
.contact-item .icon{width:48px;height:48px;border-radius:50%;background:#ececec;display:flex;align-items:center;justify-content:center}
.field{position:absolute;background:var(--field);border:1px solid var(--field-line);font-size:16px;color:var(--muted);padding:10px 16px}
.contact .btn,.footer .btn{position:absolute}
/* footer */
.footer-brand{position:absolute;left:112px;top:3022px}
.footer-brand .brand-name{font-size:32px}
.footer-col{position:absolute;top:3015px}
.footer-col h4{font-size:19px;font-weight:700;color:var(--ink);letter-spacing:.5px;margin-bottom:28px}
.footer-col li{list-style:none;font-size:18px;line-height:34px;color:var(--ink)}
.footer-rule{position:absolute;left:0;top:3282px;width:1200px;height:1px;background:#ccc}
.copyright{position:absolute;left:0;top:3302px;width:1200px;text-align:center;font-size:16px;color:var(--ink)}
</style>
</head>
<body>
<div class="page">

  <header class="hero">
    <div class="hero-photo" role="img" aria-label="Craftsman style house with a lit porch at dusk among tall pine trees"></div>
    <div class="hero-shade"></div>
    <div class="topbar">
      <div class="brand"><span class="brand-mark"></span><span class="brand-name">Oakline Builders</span></div>
      <nav class="nav">
        <a class="active" href="#">HOME</a><a href="#">ABOUT US</a><a href="#">SERVICES</a><a href="#">CONTACT US</a>
      </nav>
    </div>
    <h1 class="hero-title">WELCOME TO<br>OAKLINE BUILDERS</h1>
  </header>

  <section class="about">
    <h2 class="rule-title">ABOUT US</h2>
    <p>Lorem ipsum dolor sit amet, consectetur adipiscing elit, sed do eiusmod tempor incididunt ut labore et dolore magna aliqua. Ut enim ad minim veniam, quis nostrud exercitation ullamco laboris nisi ut aliquip ex ea commodo consequat. Duis aute</p>
    <div class="btn">READ MORE</div>
    <div class="about-photo" role="img" aria-label="Bright modern kitchen with wood cabinets, marble backsplash and pendant lights"></div>
  </section>

  <section class="services">
    <h2 class="services-title">OUR SERVICES</h2>
    <div class="service" style="left:95px"><div class="circle c-bath" role="img" aria-label="Bright bathroom with freestanding tub"></div><h3>Bathroom<br>Remodeling</h3></div>
    <div class="service" style="left:344px"><div class="circle c-kitchen" role="img" aria-label="Kitchen with dark island and bar stools"></div><h3>Kitchen<br>Remodeling</h3></div>
    <div class="service" style="left:593px"><div class="circle c-base" role="img" aria-label="Finished basement living area with sofa"></div><h3>Basment<br>Remodeling</h3></div>
    <div class="service" style="left:841px"><div class="circle c-bed" role="img" aria-label="Warm bedroom with chandelier and bed"></div><h3>Bedroom<br>Remodeling</h3></div>
  </section>

  <section class="projects">
    <h2 class="rule-title">OUR PROJECTS</h2>
    <div class="project p-kitchen" style="left:112px" role="img" aria-label="Wood kitchen project">KITCHEN</div>
    <div class="project p-bath" style="left:441px" role="img" aria-label="Dark tiled bathroom project">BATHROOM</div>
    <div class="project p-kids" style="left:770px" role="img" aria-label="Kids room with bunk bed project">KIDSROOM</div>
    <div class="dots"><span></span><span></span><span></span></div>
  </section>

  <section class="contact">
    <h2 class="contact-title">CONTACT US</h2>
    <p class="contact-text">Lorem ipsum dolor sit amet, consectetur adipiscing elit, sed do eiusmod tempor incididunt ut labore et dolore magna aliqua. Ut enim ad minim veniam, quis</p>
    <div class="contact-item" style="top:2768px">
      <span class="icon"><svg width="26" height="20" viewBox="0 0 26 20" fill="none" stroke="#666" stroke-width="2"><rect x="1" y="1" width="24" height="18" rx="3"/><path d="M2 3l11 8 11-8"/></svg></span>
      info@oaklinebuilders.com
    </div>
    <div class="contact-item" style="top:2844px">
      <span class="icon"><svg width="22" height="22" viewBox="0 0 24 24" fill="none" stroke="#666" stroke-width="1.8"><path d="M5 2h4l2 5-3 2a12 12 0 0 0 7 7l2-3 5 2v4a2 2 0 0 1-2 2A19 19 0 0 1 3 4a2 2 0 0 1 2-2z"/></svg></span>
      info@oaklinebuilders.com
    </div>
    <div class="field" style="left:599px;top:2580px;width:240px;height:41px">First Name</div>
    <div class="field" style="left:849px;top:2580px;width:240px;height:41px">First Name</div>
    <div class="field" style="left:599px;top:2640px;width:240px;height:41px">Email</div>
    <div class="field" style="left:849px;top:2640px;width:240px;height:41px">Phone No</div>
    <div class="field" style="left:599px;top:2700px;width:490px;height:110px">Message</div>
    <div class="btn" style="left:909px;top:2836px;width:180px;height:54px">SUBMIT</div>
  </section>

  <footer class="footer">
    <div class="footer-brand brand"><span class="brand-mark" style="width:40px;height:40px"></span><span class="brand-name">Oakline Builders</span></div>
    <div class="field" style="left:112px;top:3120px;width:380px;height:52px;padding-top:15px">Email</div>
    <div class="btn" style="left:112px;top:3191px;width:180px;height:54px">SUBMIT</div>
    <div class="footer-col" style="left:583px">
      <h4>QUICK LINKS</h4>
      <ul><li>Home</li><li>About Us</li><li>Services</li><li>Contac Us</li></ul>
    </div>
    <div class="footer-col" style="left:882px">
      <h4>OUR SEVICES</h4>
      <ul><li>Bathroom Modeling</li><li>Kitchen Modeling</li><li>Bedroom Modeling</li><li>Basement Modeling</li></ul>
    </div>
    <div class="footer-rule"></div>
    <p class="copyright">CopyRight@2023 Oakline Builders. All Right Reserved</p>
  </footer>

</div>
</body>
</html>
```